Motivational Poster Series for Students at Truck Driving School

We are looking for a series of 3 motivational posters (18"X 24") to be used in classrooms at a truck driving school. The audience for the posters will be the students that are currently in school and the purpose of the posters is to be motivational pieces that will be displayed on the walls.

We have provided the quotes below that are to be used on each poster. We have also provided some example images from PixVaultImages to give an idea on the backgrounds that we'd like to see on each poster. The images do not have to be exact, these are just examples of what we think will look good for each quote. Since this is a series, they can all be somewhat similar in look/feel - just with different images and quotes.

So, the basic idea is a background image/design with a quote being the main point of emphasis. Other than that, we would like to include the logo provided at a small scale in one of the corners of the poster as a watermark for branding purposes.

Below are the quotes for each of the 3 posters:

Poster 1 - “It’s very difficult to follow our dreams, but it’s even more difficult to forget them.” - Devan Okafor

Poster 2 - “Success doesn’t just come and find you, you have to go out and get it.” - Unknown

Poster 3 - “If you are not willing to learn, no one can help you. If you are determined to learn, no one can stop you.”
- Unknown

NOTE: these posters should be designed as 18" X 24" in size with 2 of them being landscape and one being portrait orientation (as shown in images provided below)

Below are some sample images to give an idea on what could be used as background design for each quote. The logo that should be used as a watermark in a corner for some subtle branding has been provided as well.

Target Market(s)

The target market for this series are truck drivers between the ages of 25-55. Mostly males.

Industry/Entity Type

Landscape

Requirements
Must have
• Quote featured, high quality background design/image, logo watermark

```html
<!DOCTYPE html>
<html lang="en">
<head>
<meta charset="UTF-8">
<title>Follow Your Dreams – Motivational Poster</title>
<link rel="stylesheet" href="https://fonts.googleapis.com/css2?family=Open+Sans:ital,wght@0,400;0,700;1,700&display=swap">
<style>
  :root {
    --sky-top: #4b4f6c;
    --sky-mid: #7c4a5e;
    --cloud-red: #b23e3c;
    --glow-orange: #e4612b;
    --horizon-gold: #f6c245;
    --ground: #1d1614;
    --quote-white: rgba(255, 255, 255, 0.86);
    --mark-white: rgba(255, 255, 255, 0.34);
    --brand-plate: rgba(200, 200, 200, 0.82);
    --brand-ink: #2a2a2a;
  }
  html, body {
    margin: 0;
    padding: 0;
    overflow: hidden;
    background: #000;
  }
  .poster {
    position: relative;
    width: 1200px;
    height: 900px;
    overflow: hidden;
    font-family: "Open Sans", Arial, sans-serif;
  }
  .backdrop {
    position: absolute;
    inset: 0;
    background:
      linear-gradient(180deg,
        var(--sky-top) 0%,
        var(--sky-mid) 22%,
        var(--cloud-red) 45%,
        var(--glow-orange) 68%,
        var(--horizon-gold) 80%,
        #c8552a 83%,
        var(--ground) 86%,
        var(--ground) 100%);
  }
  .quote-mark {
    position: absolute;
    font-weight: 700;
    font-size: 330px;
    line-height: 1;
    color: var(--mark-white);
  }
  .quote-mark--open { left: -4px; top: -12px; }
  .quote-mark--close { left: 975px; top: 418px; }
  .quote-block {
    margin: 0;
  }
  .quote-line {
    position: absolute;
    left: 0;
    width: 1200px;
    margin: 0;
    text-align: center;
    white-space: nowrap;
    font-weight: 700;
    line-height: 1;
    color: var(--quote-white);
  }
  .quote-line--1 { top: 29px; font-size: 146px; letter-spacing: -1.5px; }
  .quote-line--2 { top: 203px; font-size: 110px; letter-spacing: -0.5px; }
  .quote-line--3 { top: 352px; font-size: 86px; letter-spacing: -0.5px; }
  .quote-line--4 { top: 454px; left: -10px; font-size: 142px; font-style: italic; }
  .attribution {
    position: absolute;
    right: 16px;
    top: 659px;
    margin: 0;
    font-size: 46px;
    font-weight: 400;
    line-height: 1;
    color: var(--quote-white);
  }
  .brand {
    position: absolute;
    left: 18px;
    top: 816px;
    width: 258px;
    height: 64px;
    display: flex;
    align-items: center;
    gap: 8px;
    padding: 0 10px;
    box-sizing: border-box;
    background: var(--brand-plate);
  }
  .brand-square {
    width: 24px;
    height: 24px;
    background: var(--brand-ink);
    flex: none;
  }
  .brand-name {
    font-size: 14px;
    font-weight: 700;
    color: var(--brand-ink);
    white-space: nowrap;
  }
</style>
</head>
<body>
  <main class="poster">
    <div class="backdrop" role="img" aria-label="Photograph of a desert highway at sunset with a truck silhouetted against a red and orange sky"></div>

    <span class="quote-mark quote-mark--open" aria-hidden="true">&ldquo;</span>
    <span class="quote-mark quote-mark--close" aria-hidden="true">&rdquo;</span>

    <blockquote class="quote-block">
      <p class="quote-line quote-line--1">It’s very difficult</p>
      <p class="quote-line quote-line--2">to follow our dreams,</p>
      <p class="quote-line quote-line--3">but it’s even more difficult</p>
      <p class="quote-line quote-line--4">to forget them.</p>
    </blockquote>
    <p class="attribution">-Devan Okafor</p>

    <div class="brand">
      <span class="brand-square" aria-hidden="true"></span>
      <span class="brand-name">Roadline Driver Academy</span>
    </div>
  </main>
</body>
</html>
```